Business card and stationary designs for Harbor Summit Mentor
Harbor Summit Mentor
Business card and stationary designs for Harbor Summit Mentor - Consulting
Creative Brief
Professional
Reed Calloway
Executive & Professional Coach
4187 Willow Bend Lane Dallas TX 75231
RCalloway@harborsummitmentor.example
www.HarborSummitMentor.example
I want this to look clean, cutting edge, and for the design to stand out.
On the back of the business card I would like my logo and the phrase "Executive & Professional Coaching"

```html
<!DOCTYPE html>
<html lang="en">
<head>
<meta charset="utf-8">
<title>Harbor Summit Mentor – Business Card</title>
<link rel="stylesheet" href="https://fonts.googleapis.com/css2?family=Open+Sans:wght@400;600&display=swap">
<style>
  :root {
    --backdrop: #d8d3cb;
    --card: #e6e5e2;
    --band: #4a4a4a;
    --ink: #3b3b3b;
    --ink-soft: #6a6a6a;
    --paper-text: #ffffff;
    --band-text: #dcdcdc;
  }
  * { box-sizing: border-box; margin: 0; padding: 0; }
  html, body { width: 1200px; height: 545px; overflow: hidden; }
  body {
    background: var(--backdrop);
    font-family: "Open Sans", Arial, sans-serif;
    color: var(--ink);
    position: relative;
  }
  .card {
    position: absolute;
    top: 112px;
    width: 500px;
    height: 320px;
    background: var(--card);
    border-radius: 12px;
    overflow: hidden;
    box-shadow: 0 4px 18px rgba(0,0,0,0.12);
  }
  .card--front { left: 88px; }
  .card--back { left: 612px; }

  .brand {
    position: absolute;
    top: 58px;
    left: 0; right: 0;
    display: flex;
    align-items: center;
    justify-content: center;
    gap: 14px;
  }
  .brand__mark {
    width: 30px; height: 30px;
    border-radius: 50%;
    background: var(--ink);
  }
  .brand__name {
    font-weight: 600;
    font-size: 27px;
    letter-spacing: 1.5px;
    text-transform: uppercase;
    color: var(--ink);
  }

  .band {
    position: absolute;
    top: 158px;
    left: 0; right: 0;
    height: 110px;
    background: var(--band);
    color: var(--paper-text);
  }
  .holder {
    position: absolute;
    left: 32px;
    top: 26px;
    font-size: 13px;
    line-height: 1.45;
  }
  .holder__name {
    font-weight: 600;
    font-size: 16px;
    text-transform: uppercase;
    letter-spacing: 0.5px;
  }
  .holder__role { color: var(--band-text); }
  .contact {
    position: absolute;
    left: 262px;
    top: 16px;
    font-size: 10px;
    line-height: 1.55;
    color: var(--band-text);
  }
  .contact__gap { height: 6px; }

  .website {
    position: absolute;
    bottom: 18px;
    left: 32px;
    font-size: 16px;
    color: var(--ink-soft);
    letter-spacing: 0.3px;
  }

  .tagline {
    position: absolute;
    top: 0; bottom: 0; left: 0; right: 0;
    display: flex;
    align-items: center;
    justify-content: center;
    font-size: 17px;
    color: var(--paper-text);
  }
</style>
</head>
<body>
  <section class="card card--front" aria-label="Business card front">
    <div class="brand">
      <span class="brand__mark"></span>
      <span class="brand__name">Harbor Summit Mentor</span>
    </div>
    <div class="band">
      <div class="holder">
        <p class="holder__name">Reed Calloway</p>
        <p class="holder__role">Executive &amp; Professional</p>
        <p class="holder__role">COACH</p>
      </div>
      <div class="contact">
        <p>4187 Willow Bend Lane</p>
        <p>Dallas TX 75231</p>
        <div class="contact__gap"></div>
        <p>Toll free: 1-800-555-0148</p>
        <p>Cell:&nbsp;&nbsp;&nbsp;&nbsp;&nbsp;&nbsp;&nbsp;214-555-0172</p>
        <div class="contact__gap"></div>
        <p>RCalloway@harborsummitmentor.example</p>
      </div>
    </div>
    <p class="website">www.HarborSummitMentor.example</p>
  </section>

  <section class="card card--back" aria-label="Business card back">
    <div class="brand">
      <span class="brand__mark"></span>
      <span class="brand__name">Harbor Summit Mentor</span>
    </div>
    <div class="band">
      <p class="tagline">Executive &amp; Professional Coaching</p>
    </div>
  </section>
</body>
</html>
```